Modern corporate energy/fuel business need business card design

Business card required for company founder. Korvan Specialised Energy is a Australian based modern energy/fuel provider. We offer specialised solutions to businesses using fossil fuels through renewable energy solutions.

I would like one side with specific information (name, address etc)

The other side to be bold, professional company name & logo. Striking.

Target Market(s)

B2B. Transport, mining, councils, environmentalist,

Industry/Entity Type

Petroleum

Contact Information for Business Card

Name; Oliver Brentham
Position; Director
Email; obrentham@korvanspec.com.au
Address; PO Box 487, Penrith, NSW, 2751
Website; www.korvanspec.com.au

Colors

Designer to choose colors to be used in the design.

Requirements
Must have
• Clean, easy to read, professional & strong theme
Should not have
• too many colours, busy layout,

```html
<!DOCTYPE html>
<html lang="en">
<head>
<meta charset="utf-8">
<title>Korvan Integrated Energy – Business Card</title>
<link href="https://fonts.googleapis.com/css2?family=Lato:wght@400;700&display=swap" rel="stylesheet">
<style>
  :root {
    --backdrop: #2b2b2b;
    --card-white: #ffffff;
    --navy: #1f4a72;
    --orange: #f47a20;
    --orange-light: #ff9a45;
    --orange-deep: #ff6f0f;
    --ink: #222222;
    --rule: #a8a8a8;
  }
  * { margin: 0; padding: 0; box-sizing: border-box; }
  html, body { width: 1200px; height: 1200px; overflow: hidden; }
  body {
    background: var(--backdrop);
    font-family: "Lato", sans-serif;
    position: relative;
  }
  .card {
    position: absolute;
    top: 310px;
    width: 364px;
    height: 594px;
    box-shadow: 0 4px 10px rgba(0,0,0,0.5);
  }
  .card-front { left: 234px; background: var(--card-white); }
  .card-back {
    left: 627px;
    width: 369px;
    background:
      radial-gradient(ellipse 70% 45% at 55% 45%, rgba(255,170,90,0.55), transparent 70%),
      linear-gradient(160deg, var(--orange-light) 0%, var(--orange-deep) 45%, var(--orange-light) 100%);
  }

  .brand {
    position: absolute;
    display: flex;
    align-items: center;
    gap: 10px;
  }
  .brand-front { left: 30px; top: 158px; color: var(--navy); }
  .brand-dot {
    width: 70px; height: 70px; border-radius: 50%;
    background: var(--orange);
    flex: none;
  }
  .brand-name { display: flex; flex-direction: column; line-height: 1; }
  .brand-name .word { font-weight: 700; }
  .brand-name .tagline { font-weight: 400; }
  .brand-front .brand-name .word { font-size: 40px; letter-spacing: 5px; }
  .brand-front .brand-name .tagline { font-size: 11px; letter-spacing: 6.6px; margin-top: 6px; }

  .contact {
    position: absolute;
    left: 0; right: 0; top: 372px;
    text-align: center;
  }
  .person-name { color: var(--navy); font-weight: 700; font-size: 22px; letter-spacing: -0.3px; }
  .person-role { color: var(--orange); font-size: 16px; margin-top: -2px; }
  .divider { width: 182px; height: 1px; background: var(--rule); margin: 10px auto; }
  .email { color: var(--ink); font-size: 16px; margin-top: 12px; }
  .web { color: var(--navy); font-size: 16px; }
  .web .accent { color: var(--orange); }
  .address { color: var(--ink); font-size: 17px; margin-top: 20px; }

  .brand-back { left: 40px; top: 472px; color: #ffffff; }
  .brand-back .brand-name .word { font-size: 48px; letter-spacing: 8px; }
  .brand-back .brand-name .tagline { font-size: 14px; letter-spacing: 7.6px; margin-top: 10px; }
</style>
</head>
<body>
  <section class="card card-front">
    <div class="brand brand-front">
      <span class="brand-dot"></span>
      <div class="brand-name">
        <span class="word">KORVAN</span>
        <span class="tagline">INTEGRATED ENERGY</span>
      </div>
    </div>
    <div class="contact">
      <p class="person-name">OLIVER BRENTHAM</p>
      <p class="person-role">Director</p>
      <div class="divider"></div>
      <p class="email">obrentham@korvanspec.com.au</p>
      <p class="web">www.<span class="accent">korvanspec</span>.com.au</p>
      <div class="divider"></div>
      <p class="address">PO Box 487, Marlow Vale QLD, 4305</p>
    </div>
  </section>

  <section class="card card-back">
    <div class="brand brand-back">
      <div class="brand-name">
        <span class="word">KORVAN</span>
        <span class="tagline">INTEGRATED ENERGY</span>
      </div>
    </div>
  </section>
</body>
</html>
```